Personal Cards

I'm looking to create personal business cards that I'll used just to pass out information, but I kind of wanted to also work in the fact that I'm a software developer.

Looking for a double-sided business card design. I'm thinking this will be printed on a nice matted cardstock. Black front, open to ideas on the back color. I'd like a logo or stamp design worked in on the front that would look good with raised ink. I'm thinking black raised ink on the black background. Also on the front, I just want the name "Telmorinx" with no other information.

On the back, the following information:
Calvin Brumley
Software Engineer
555-246-8093
cbrumley@telmorinx.example

I'm open to working in a nice QR code on the back; I've seen some stylized QR codes out there that I really like. I like designs that bleed off the edge, and designs that aren't too organized and starchy. I also like minimalism, but I'm not married to the idea.
Updates

oh, please include my facebook on the contact infos: www.facebook.com/quiloberth

Industry/Entity Type

Business

```html
<!DOCTYPE html>
<html lang="en">
<head>
<meta charset="utf-8">
<title>Telmorinx Business Card</title>
<link rel="stylesheet" href="https://fonts.googleapis.com/css2?family=Inter:wght@200;300&display=swap">
<style>
  :root {
    --page-bg: #ffffff;
    --front-bg: #333333;
    --front-ink: #1c1c1c;
    --back-bg: #b3dff2;
    --back-accent: #9ed4ec;
    --back-ink: #1d1d1d;
  }
  * { margin: 0; padding: 0; box-sizing: border-box; }
  html, body {
    width: 848px;
    height: 1200px;
    overflow: hidden;
    background: var(--page-bg);
  }
  .sheet {
    position: relative;
    width: 848px;
    height: 1200px;
    font-family: "Inter", "Helvetica Neue", Arial, sans-serif;
  }
  .card {
    position: absolute;
    left: 44px;
    width: 760px;
    height: 459px;
    overflow: hidden;
  }
  .card-front {
    top: 107px;
    background: var(--front-bg);
  }
  .brand-dot {
    position: absolute;
    left: 50%;
    top: 100px;
    width: 150px;
    height: 150px;
    margin-left: -75px;
    border: 4px solid var(--front-ink);
    border-radius: 50%;
  }
  .brand-name {
    position: absolute;
    left: 0;
    right: 0;
    top: 282px;
    text-align: center;
    font-weight: 200;
    font-size: 72px;
    letter-spacing: -1px;
    color: var(--front-ink);
  }
  .card-back {
    top: 610px;
    background: var(--back-bg);
  }
  .back-accent {
    position: absolute;
    left: -140px;
    top: 40px;
    width: 420px;
    height: 420px;
    border: 9px solid var(--back-accent);
    border-radius: 50%;
  }
  .contact {
    position: absolute;
    left: 274px;
    top: 238px;
    list-style: none;
    font-weight: 200;
    font-size: 36px;
    line-height: 45px;
    letter-spacing: -0.4px;
    color: var(--back-ink);
  }
</style>
</head>
<body>
  <main class="sheet">
    <section class="card card-front">
      <div class="brand-dot"></div>
      <h1 class="brand-name">Telmorinx</h1>
    </section>
    <section class="card card-back">
      <div class="back-accent"></div>
      <ul class="contact">
        <li class="contact-name">Calvin Brumley</li>
        <li class="contact-role">Software Engineer</li>
        <li class="contact-phone">555-246-8093</li>
        <li class="contact-email">cbrumley@telmorinx.example</li>
      </ul>
    </section>
  </main>
</body>
</html>
```